Email Signature and a letter head

I need a professional email signature and a letter head for letters sent by post. I've attached my logo and a signature i am currently using. Current letter head is also attached.

Target Market(s)

Accounting Clients

Industry/Entity Type

Public Accounting

Font styles to use
Sans Serif

Colors

Designer to choose colors to be used in the design.

Requirements
Must have
• My logo, RJ Logo, Plumo Logo, Tax Agent logo. All attached.
• All my credentials - examples in the attached documents

```html
<!DOCTYPE html>
<html lang="en">
<head>
<meta charset="utf-8">
<title>Summit Ledger Letterhead</title>
<link href="https://fonts.googleapis.com/css2?family=Didact+Gothic&family=Roboto:wght@400;500;700&display=swap" rel="stylesheet">
<style>
  :root {
    --ink: #141414;
    --gold: #c9a43a;
    --yellow: #fdc654;
    --paper: #ffffff;
    --body: #555555;
    --muted: #8a8a8a;
    --sky: #1fb3e0;
    --teal: #1a7f9a;
    --brand-red: #e2413a;
    --bg: #ffffff;
  }
  * { margin: 0; padding: 0; box-sizing: border-box; }
  html, body { width: 1200px; height: 1172px; overflow: hidden; background: var(--bg); }
  .canvas { position: relative; width: 1200px; height: 1172px; }
  .sheet { position: absolute; background: var(--paper); overflow: hidden; }
  .sheet--first { left: 27px; top: 21px; width: 688px; height: 963px; }
  .sheet--next { left: 507px; top: 211px; width: 630px; height: 879px; }
  .sheet__shapes { position: absolute; inset: 0; }

  .brand { position: absolute; width: 200px; display: flex; flex-direction: column; align-items: center; font-family: "Didact Gothic", sans-serif; color: var(--gold); text-transform: uppercase; }
  .brand__mark { width: 76px; height: 76px; border: 2.5px solid var(--gold); border-radius: 50%; }
  .brand__name { margin-top: 8px; font-size: 20px; line-height: 22px; letter-spacing: 0.5px; white-space: nowrap; }
  .brand__tag { font-size: 9.5px; letter-spacing: 2.6px; line-height: 12px; white-space: nowrap; }

  .contacts { position: absolute; right: 24px; list-style: none; font-family: "Didact Gothic", sans-serif; color: var(--gold); font-size: 11.5px; }
  .contacts li { display: flex; justify-content: flex-end; align-items: center; gap: 8px; height: 24px; white-space: nowrap; }
  .contacts svg { width: 17px; height: 17px; flex: none; }

  .recipient { position: absolute; left: 48px; top: 260px; font-family: "Roboto", sans-serif; font-size: 12.5px; line-height: 15px; color: var(--ink); font-style: normal; }
  .recipient__name { font-weight: 700; }
  .recipient__role, .recipient__phone { color: var(--muted); font-weight: 500; letter-spacing: 0.6px; }

  .letter-body { position: absolute; left: 48px; top: 370px; width: 640px; font-family: "Roboto", sans-serif; font-size: 12.3px; line-height: 15.6px; color: var(--body); white-space: nowrap; }
  .letter-body p { margin-bottom: 14px; }

  .signature { position: absolute; left: 48px; top: 752px; width: 206px; height: 68px; background: linear-gradient(90deg, #e9e9e9, #f4f4f4); border-radius: 4px; }

  .signoff { position: absolute; font-family: "Didact Gothic", sans-serif; color: var(--ink); white-space: nowrap; }
  .signoff__name { font-size: 14.5px; }
  .signoff__name small { font-size: 12px; }
  .signoff__ids { font-size: 13px; margin-top: 4px; }

  .partners { position: absolute; display: flex; align-items: center; gap: 10px; font-family: "Didact Gothic", sans-serif; color: var(--ink); }
  .partner { display: flex; align-items: center; gap: 5px; font-size: 13px; }
  .partner__dot { width: 12px; height: 12px; border-radius: 50%; }
  .partner__dot--red { background: var(--brand-red); }
  .partner__dot--sky { background: var(--sky); }
  .badge { width: 44px; height: 44px; border-radius: 50%; }
  .badge--teal { background: var(--teal); }
  .badge--tpb { background: #f1f1f1; border: 3px solid #333; }
  .tax-agent { font-size: 10px; line-height: 12px; font-weight: 700; font-family: "Roboto", sans-serif; }
</style>
</head>
<body>
<main class="canvas">

  <section class="sheet sheet--first">
    <svg class="sheet__shapes" viewBox="0 0 688 963" width="688" height="963" aria-hidden="true">
      <polygon points="0,0 688,0 688,155 0,213" fill="var(--ink)"/>
      <polygon points="0,846 477,963 0,963" fill="var(--yellow)"/>
    </svg>

    <div class="brand" style="left:22px; top:30px;">
      <span class="brand__mark"></span>
      <span class="brand__name">Summit Ledger</span>
      <span class="brand__tag">Business Services</span>
    </div>

    <ul class="contacts" style="top:30px;">
      <li>0400 123 987 <svg viewBox="0 0 20 20"><circle cx="10" cy="10" r="10" fill="var(--yellow)"/><path d="M6.5 5.5l2 -.5 1 2.5-1.2 1a6 6 0 0 0 3.2 3.2l1-1.2 2.5 1-.5 2c-4.5.3-8.3-3.5-8-8z" fill="var(--ink)"/></svg></li>
      <li>marlow@summitledgerservices.com.au <svg viewBox="0 0 20 20"><circle cx="10" cy="10" r="10" fill="var(--yellow)"/><rect x="5" y="6.5" width="10" height="7" fill="var(--ink)"/><path d="M5 6.5l5 4 5-4" stroke="var(--yellow)" fill="none"/></svg></li>
      <li>www.summitledgerservices.com.au <svg viewBox="0 0 20 20"><circle cx="10" cy="10" r="10" fill="var(--yellow)"/><circle cx="10" cy="10" r="5" fill="none" stroke="var(--ink)" stroke-width="1.6"/><path d="M10 5v10M5 10h10" stroke="var(--ink)" stroke-width="1.2"/></svg></li>
      <li>18 Harbour Lane, Seaview East VIC 3940 <svg viewBox="0 0 20 20"><circle cx="10" cy="10" r="10" fill="var(--yellow)"/><path d="M10 15.5s-4-4.2-4-7a4 4 0 0 1 8 0c0 2.8-4 7-4 7z" fill="var(--ink)"/><circle cx="10" cy="8.5" r="1.5" fill="var(--yellow)"/></svg></li>
    </ul>

    <address class="recipient">
      <div>To</div>
      <div class="recipient__name">Daniel Reed,</div>
      <div class="recipient__role">CEO, BRIGHTFORM STUDIO</div>
      <div class="recipient__phone">M: +91 70000 12345</div>
    </address>

    <div class="letter-body">
      <p>Solum nullam principes vis no, eleifend postulant mediocrem ut est, ad tota partem<br>scribentur no, mea meis solet melius no, pri feugait noluisse appetere no.Ei mea<br>probatus est et. Duo ut oportere iudicabit, exerci laoreet vim id. An vidit quidam<br>ea. Mollis incorrupte in vix. Noster mnesarchum vix ei.</p>
      <p>Lus te maluisset voluptatum quaerendum, no discere saperet persequeris cum<br>phaedrum. Mel mazim corpora te. Has ad aeque mucius impetus,<br>vel tation regione appetere ne. Porro voluptatum ius ut, ei docendi eloquentiam<br>sim efficiendi eum, est id tota insolens, eu per facete latine.</p>
      <p>Sea te explicari conceptam definitionem, soluta constituto duo ad, usu an laudem<br>magna repudiare forensibus an.<br>In nam euismod explicari voluptatibus. Petentium dissentiet ex eum, in eam ludus<br>latine feugait suavitate.</p>
      <p>Eum ei augue voluptua copiosae. Vis cu altera noluisse intellegat. At vis probatus<br>interesset ne quo, est ad exerci oblique recusabo, eu sit simul legendos antiopam<br>ad, delectus sapientem omittantur ut vis. Pro te graece equidem ancillae, indoctum</p>
      <p>Sea te explicari conceptam definitionem, soluta constituto duo ad, usu an laudem<br>magna repudiare forensibus an. In nam euismod explicari voluptatibus. Petentium<br>eam ludus tantas aperiam. Eu est latine feugait suavitate.</p>
    </div>

    <div class="signature" role="img" aria-label="Handwritten signature of Marlow Hayes"></div>

    <div class="signoff" style="left:20px; top:898px;">
      <div class="signoff__name">Marlow Hayes,<small>RJ BBus</small></div>
      <div class="signoff__ids">ABN: 12 345 678 901, TAN: 987 654 32</div>
    </div>

    <div class="partners" style="left:345px; top:890px;">
      <span class="partner"><span class="partner__dot partner__dot--red"></span>RJ</span>
      <span class="partner" style="margin-left:30px;"><span class="partner__dot partner__dot--sky"></span>Plumo</span>
    </div>
  </section>

  <section class="sheet sheet--next">
    <svg class="sheet__shapes" viewBox="0 0 630 879" width="630" height="879" aria-hidden="true">
      <polygon points="0,0 630,0 630,123 0,193" fill="var(--ink)"/>
      <polygon points="0,773 430,879 0,879" fill="var(--yellow)"/>
    </svg>

    <div class="brand" style="left:12px; top:28px;">
      <span class="brand__mark"></span>
      <span class="brand__name">Summit Ledger</span>
      <span class="brand__tag">Business Services</span>
    </div>

    <ul class="contacts" style="top:24px;">
      <li>0400 123 987 <svg viewBox="0 0 20 20"><circle cx="10" cy="10" r="10" fill="var(--yellow)"/><path d="M6.5 5.5l2 -.5 1 2.5-1.2 1a6 6 0 0 0 3.2 3.2l1-1.2 2.5 1-.5 2c-4.5.3-8.3-3.5-8-8z" fill="var(--ink)"/></svg></li>
      <li>marlow@summitledgerservices.com.au <svg viewBox="0 0 20 20"><circle cx="10" cy="10" r="10" fill="var(--yellow)"/><rect x="5" y="6.5" width="10" height="7" fill="var(--ink)"/><path d="M5 6.5l5 4 5-4" stroke="var(--yellow)" fill="none"/></svg></li>
      <li>www.summitledgerservices.com.au <svg viewBox="0 0 20 20"><circle cx="10" cy="10" r="10" fill="var(--yellow)"/><circle cx="10" cy="10" r="5" fill="none" stroke="var(--ink)" stroke-width="1.6"/><path d="M10 5v10M5 10h10" stroke="var(--ink)" stroke-width="1.2"/></svg></li>
      <li>18 Harbour Lane, Seaview East VIC 3940 <svg viewBox="0 0 20 20"><circle cx="10" cy="10" r="10" fill="var(--yellow)"/><path d="M10 15.5s-4-4.2-4-7a4 4 0 0 1 8 0c0 2.8-4 7-4 7z" fill="var(--ink)"/><circle cx="10" cy="8.5" r="1.5" fill="var(--yellow)"/></svg></li>
    </ul>

    <div class="signoff" style="left:22px; top:822px;">
      <div class="signoff__name">Marlow Hayes,<small>RJ BBus</small></div>
      <div class="signoff__ids">ABN: 12 345 678 901, TAN: 987 654 32</div>
    </div>

    <div class="partners" style="left:300px; top:794px;">
      <span class="partner"><span class="partner__dot partner__dot--red"></span>RJ</span>
      <span class="partner" style="margin-left:8px;"><span class="partner__dot partner__dot--sky"></span>Plumo</span>
      <span class="badge badge--teal"></span>
      <span class="badge badge--tpb" style="margin-left:6px;"></span>
      <span class="tax-agent">Tax agent<br>10293847</span>
    </div>
  </section>

</main>
</body>
</html>
```